Kestrow Fire Services Pty Ltd

We need business cards for a company based in Perth, we install, service and maintain fire equipment.
On the front we want a great design with our logo and a small spot for our full company name, general company email address and office number. On the back we need space for our name, title, mobile number and email address on the back.

Target Market(s)

Facility managers and commercial/industrial building owners/occupiers.

Contact Information for Business Card

Font styles to use
Sans Serif

Requirements
Must have
• Please only submit 5 of your best samples.
Darker tones are preferred.
Nice to have
• We want to use, black, red and grey. Keep it modern and clean.
I've attached the company logo and a sample of a boarder we use on our emergency plans.
Should not have
• No preference. Let the designer choose.

```html
<!DOCTYPE html>
<html lang="en">
<head>
<meta charset="utf-8">
<title>Kestrow Fire Services – Business Cards</title>
<link rel="stylesheet" href="https://fonts.googleapis.com/css2?family=Arimo:wght@400;700&display=swap">
<style>
  :root {
    --stage: #bcbcbc;
    --fire-red: #e81b24;
    --red-shade: #dc1b24;
    --white: #ffffff;
    --ink: #2b2b2b;
    --mist: #e6e6e6;
    --radius: 30px;
  }
  * { box-sizing: border-box; margin: 0; padding: 0; }
  html, body { width: 1200px; height: 900px; overflow: hidden; }
  body {
    background: var(--stage);
    font-family: "Arimo", Arial, sans-serif;
    display: flex;
    flex-direction: column;
    align-items: center;
    justify-content: center;
    gap: 44px;
  }
  .card {
    position: relative;
    width: 660px;
    height: 377px;
    border-radius: var(--radius);
    overflow: hidden;
    box-shadow: 0 6px 14px rgba(0,0,0,0.28);
  }
  .card--front { background: var(--fire-red); color: var(--white); }
  .card--back { background: var(--white); color: var(--ink); }

  .backdrop-block {
    position: absolute;
    right: -40px;
    top: -30px;
    width: 330px;
    height: 330px;
  }
  .card--front .backdrop-block { background: var(--red-shade); }
  .card--back .backdrop-block { background: var(--mist); }

  .content {
    position: absolute;
    left: 56px;
    top: 70px;
  }
  .wordmark {
    font-weight: 700;
    font-size: 58px;
    letter-spacing: 1px;
    line-height: 1;
    display: flex;
    align-items: center;
    gap: 14px;
  }
  .wordmark-square {
    width: 22px;
    height: 22px;
  }
  .card--front .wordmark-square { background: var(--white); }
  .card--back .wordmark { color: var(--fire-red); }
  .card--back .wordmark-square { background: var(--fire-red); }

  .company-name {
    margin-top: 44px;
    font-weight: 700;
    font-size: 21px;
    letter-spacing: 1px;
    text-transform: uppercase;
  }
  .office-phone {
    margin-top: 8px;
    font-weight: 700;
    font-size: 27px;
  }
  .contact-list {
    list-style: none;
    margin-top: 8px;
    font-size: 17px;
  }
  .contact-list li {
    display: flex;
    align-items: center;
    gap: 10px;
    line-height: 1.4;
  }
  .contact-list svg { width: 18px; height: 18px; flex: none; }

  .person-name {
    margin-top: 58px;
    color: var(--fire-red);
    font-weight: 700;
    font-size: 26px;
    text-transform: uppercase;
    letter-spacing: 0.5px;
  }
  .person-title { font-size: 20px; margin-top: 2px; }
  .card--back .contact-list { margin-top: 18px; font-size: 20px; }
  .card--back .contact-list svg { width: 20px; height: 20px; }
</style>
</head>
<body>

  <section class="card card--front">
    <div class="backdrop-block" role="img" aria-label="Large faint brand mark area"></div>
    <div class="content">
      <div class="wordmark"><span class="wordmark-square"></span>KESTROW</div>
      <p class="company-name">Kestrow Fire Services Pty Ltd</p>
      <p class="office-phone">789.4410.2260</p>
      <ul class="contact-list">
        <li>
          <svg viewBox="0 0 20 20" fill="none" stroke="#fff" stroke-width="1.8"><rect x="2" y="4" width="16" height="12"/><path d="M2 4l8 7 8-7"/></svg>
          info@kestrow.com
        </li>
        <li>
          <svg viewBox="0 0 20 20" fill="none" stroke="#fff" stroke-width="1.6"><circle cx="10" cy="10" r="8"/><ellipse cx="10" cy="10" rx="3.5" ry="8"/><path d="M2 10h16M3.5 6h13M3.5 14h13"/></svg>
          www.kestrow.com
        </li>
      </ul>
    </div>
  </section>

  <section class="card card--back">
    <div class="backdrop-block" role="img" aria-label="Large faint brand mark area"></div>
    <div class="content">
      <div class="wordmark"><span class="wordmark-square"></span>KESTROW</div>
      <p class="person-name">Marcus Hale</p>
      <p class="person-title">Managing Director</p>
      <ul class="contact-list">
        <li>
          <svg viewBox="0 0 20 20" fill="none" stroke="#e81b24" stroke-width="2"><rect x="5" y="2" width="10" height="16" rx="2"/><path d="M9 15h2"/></svg>
          789.5518.3307
        </li>
        <li>
          <svg viewBox="0 0 20 20" fill="#e81b24"><path d="M2 4h16v12H2z"/><path d="M2 4l8 7 8-7" fill="none" stroke="#fff" stroke-width="1.6"/></svg>
          marcus@kestrow.com
        </li>
      </ul>
    </div>
  </section>

</body>
</html>
```